KSI Business Card

Please create a creative design for a business card using the new theme from the Logo & website. This company's main focus is food manufacturing building construction. Please integrate the new logo attached.

Please use the following information for the demo card:

Kelvane Systems, Inc.
Doug Farnham
dfarnham@kelvanesys.example
Cell: 630-555-0193
218 Harbison Ln
Halvern, WI 60194

See pictures and more information on the website.

www.kelvanesys.example

```html
<!DOCTYPE html>
<html lang="en">
<head>
<meta charset="utf-8">
<title>KSI Business Card</title>
<link href="https://fonts.googleapis.com/css2?family=Figtree:wght@400;600;700&display=swap" rel="stylesheet">
<style>
  :root {
    --page-bg: #eeeff2;
    --card-white: #ffffff;
    --brand-blue: #1a7fcb;
    --brand-deep: #1a6fb8;
    --logo-blue: #1565ab;
    --ice-blue: #6fb1e2;
    --ice-light: #b7d5f0;
    --ink: #2a2a2a;
  }
  * { margin: 0; padding: 0; box-sizing: border-box; }
  html, body { width: 1200px; height: 800px; overflow: hidden; }
  body {
    background: var(--page-bg);
    font-family: "Figtree", sans-serif;
    position: relative;
  }
  .card {
    position: absolute;
    top: 284px;
    width: 429px;
    height: 238px;
    overflow: hidden;
  }
  .card--front { left: 111px; background: var(--card-white); }
  .card--back {
    left: 639px;
    background: linear-gradient(90deg, var(--brand-deep) 0%, #3f9ad6 35%, #6d9fd9 65%, var(--ice-light) 100%);
  }
  .accent-bar {
    position: absolute; left: 0; top: 14px;
    width: 3px; height: 210px;
    background: var(--brand-blue);
  }
  .wordmark {
    position: absolute;
    color: var(--brand-blue);
    font-weight: 700;
    line-height: 1;
  }
  .wordmark__initials { display: block; letter-spacing: 1px; }
  .wordmark__name { display: block; white-space: nowrap; }
  .wordmark__dot {
    position: absolute;
    border-radius: 50%;
    background: var(--brand-blue);
  }
  .card--front .wordmark { left: 15px; top: 20px; width: 148px; text-align: center; }
  .card--front .wordmark__initials { font-size: 42px; }
  .card--front .wordmark__name { font-size: 12.5px; margin-top: 8px; }
  .card--front .wordmark__dot { width: 8px; height: 8px; right: 22px; top: -6px; }

  .card--back .wordmark { left: 160px; top: 52px; width: 230px; text-align: center; color: var(--logo-blue); }
  .card--back .wordmark__initials { font-size: 58px; }
  .card--back .wordmark__name { font-size: 17px; margin-top: 12px; }
  .card--back .wordmark__dot { width: 10px; height: 10px; right: 42px; top: -8px; background: var(--logo-blue); }

  .holder-name {
    position: absolute; left: 15px; top: 118px;
    color: var(--brand-blue);
    font-size: 15.5px; font-weight: 700; letter-spacing: .2px;
  }
  .address {
    position: absolute; left: 15px; top: 144px;
    font-size: 11px; line-height: 14px; color: var(--ink);
    font-style: normal;
  }
  .contact-list {
    position: absolute; left: 15px; top: 185px;
    list-style: none; font-size: 11px; color: var(--ink);
  }
  .contact-list li { display: flex; align-items: center; height: 14.5px; }
  .contact-list svg { width: 11px; height: 11px; margin-right: 6px; fill: none; stroke: var(--brand-blue); stroke-width: 1.4; }
  .contact-list .web-domain { color: var(--brand-blue); font-weight: 600; }

  .ice-decor {
    position: absolute; top: 22px; height: 192px;
  }
  .card--front .ice-decor {
    right: 0; width: 108px;
    background: linear-gradient(90deg, rgba(111,177,226,0) 0%, var(--ice-blue) 70%);
    border-radius: 96px 0 0 96px;
  }
  .card--back .ice-decor {
    left: 0; width: 112px;
    background: linear-gradient(270deg, rgba(160,205,238,0) 0%, rgba(160,205,238,.75) 70%);
    border-radius: 0 96px 96px 0;
  }
</style>
</head>
<body>
  <section class="card card--front">
    <div class="accent-bar"></div>
    <div class="wordmark">
      <span class="wordmark__dot"></span>
      <span class="wordmark__initials">KSI</span>
      <span class="wordmark__name">Kelvane Systems, Inc.</span>
    </div>
    <h1 class="holder-name">DOUG FARNHAM</h1>
    <address class="address">218 Harbison Ln<br>Halvern, WI 60194</address>
    <ul class="contact-list">
      <li><svg viewBox="0 0 12 12"><rect x="3" y="1" width="6" height="10" rx="1"/><line x1="5.5" y1="9.3" x2="6.5" y2="9.3"/></svg>630-555-0193</li>
      <li><svg viewBox="0 0 12 12"><rect x="1" y="2.5" width="10" height="7"/><polyline points="1,2.5 6,6.5 11,2.5"/></svg>dfarnham@kelvanesys.example</li>
      <li><svg viewBox="0 0 12 12"><circle cx="6" cy="6" r="5"/><ellipse cx="6" cy="6" rx="2.2" ry="5"/><line x1="1" y1="6" x2="11" y2="6"/></svg>www.<span class="web-domain">kelvanesys</span>.example</li>
    </ul>
    <div class="ice-decor" role="img" aria-label="Large light blue snowflake motif cut at the card edge"></div>
  </section>

  <section class="card card--back">
    <div class="ice-decor" role="img" aria-label="Large pale blue snowflake motif cut at the card edge"></div>
    <div class="wordmark">
      <span class="wordmark__dot"></span>
      <span class="wordmark__initials">KSI</span>
      <span class="wordmark__name">Kelvane Systems, Inc.</span>
    </div>
  </section>
</body>
</html>
```